Economic Book Cover

I need a book cover for a 5.5" x 8.5" paperback book that is 100 pages long. No title or words on the spine please, as the book is too thin to print on the spine. The title of the book is The Nine Harbor Lanterns. The subtitle is "The Patient Weave of Morning Light and Quiet Harbor Stones"
We'd like the cover to have a drawing of a dove offering an olive branch to a hundred dollar bill. You could use the attached illustration or create your own. The cover should be peaceful, hopeful, with cool colors.
The back cover should have the attached book description on it.
The authors name is Derek Halvorn and should be listed only on the front cover. No author's photo or description of the author need appear on the back cover, just the book description.
American voters

```html
<!DOCTYPE html>
<html lang="en">
<head>
<meta charset="utf-8">
<title>The Nine Harbor Lanterns — Cover</title>
<link rel="stylesheet" href="https://fonts.googleapis.com/css2?family=Cinzel:wght@400;700&family=Kaushan+Script&family=Tinos&family=Arimo:ital,wght@1,700&display=swap">
<style>
  :root {
    --page-bg: #e9ece8;
    --cover-light: #a9d6a3;
    --cover-mid: #8fc78a;
    --cover-glow: #c9e8c3;
    --green-deep: #1f6b3a;
    --green-title: #2a7a43;
    --ink-dark: #1e2a22;
    --text-light: #eef7ee;
    --line: #2f7a47;
  }
  * { margin: 0; padding: 0; box-sizing: border-box; }
  html, body { width: 1200px; height: 1200px; overflow: hidden; }
  body {
    background: var(--page-bg);
    position: relative;
  }
  .cover {
    position: absolute;
    top: 229px;
    width: 480px;
    height: 742px;
    background: radial-gradient(ellipse at 55% 35%, var(--cover-glow) 0%, var(--cover-light) 45%, var(--cover-mid) 100%);
    box-shadow: 0 6px 18px rgba(0,0,0,0.18);
    overflow: hidden;
  }
  .cover--back { left: 100px; }
  .cover--front { left: 620px; }

  /* Back cover */
  .description {
    position: absolute;
    left: 40px;
    top: 66px;
    width: 400px;
    padding: 26px 30px;
    background: var(--green-deep);
    border-radius: 12px;
    color: var(--text-light);
    font-family: "Tinos", "Times New Roman", serif;
    font-size: 14.5px;
    line-height: 1.3;
  }
  .description p + p { margin-top: 16px; }

  /* Front cover */
  .title {
    position: absolute;
    left: 60px;
    top: 70px;
    width: 380px;
  }
  .title__lead {
    display: block;
    font-family: "Kaushan Script", cursive;
    font-size: 40px;
    color: var(--ink-dark);
    line-height: 1;
    margin-left: 4px;
  }
  .title__main {
    display: block;
    font-family: "Cinzel", serif;
    font-weight: 700;
    font-size: 66px;
    color: var(--green-title);
    line-height: 1;
    margin-top: 2px;
    margin-left: 30px;
  }
  .title__sub {
    display: block;
    font-family: "Cinzel", serif;
    font-weight: 700;
    font-size: 48px;
    color: var(--ink-dark);
    line-height: 1;
    margin-top: 4px;
    margin-left: 30px;
  }
  .title__rule {
    position: absolute;
    left: 40px;
    top: 262px;
    width: 400px;
    height: 2px;
    background: var(--line);
  }
  .artwork {
    position: absolute;
    left: 80px;
    top: 285px;
    width: 330px;
    height: 300px;
  }
  .author {
    position: absolute;
    right: 70px;
    top: 600px;
    font-family: "Cinzel", serif;
    font-size: 17px;
    letter-spacing: 1px;
    color: var(--ink-dark);
  }
  .author__rule {
    position: absolute;
    left: 40px;
    top: 626px;
    width: 440px;
    height: 2px;
    background: var(--line);
  }
  .subtitle-band {
    position: absolute;
    left: 40px;
    top: 636px;
    width: 440px;
    height: 54px;
    background: var(--green-deep);
    display: flex;
    align-items: center;
    padding-left: 56px;
    padding-right: 16px;
  }
  .subtitle-band__mark {
    position: absolute;
    left: 16px;
    top: 19px;
    width: 16px;
    height: 16px;
    background: var(--cover-light);
    border-radius: 50%;
  }
  .subtitle-band__text {
    font-family: "Arimo", Arial, sans-serif;
    font-style: italic;
    font-weight: 700;
    font-size: 14px;
    line-height: 1.25;
    color: var(--text-light);
    text-align: center;
    width: 100%;
  }
</style>
</head>
<body>
  <section class="cover cover--back" aria-label="Back cover">
    <div class="description">
      <p>The Nine Harbor Lanterns is a practical guide to the liberation of our nation's economic woes. Halvorn introduces an entirely new way of looking at our economy that revolutionizes our financial system, producing an unprecedented level of abundance for all.</p>
      <p>If we follow the Nine Harbor Lanterns, we can eliminate income taxes, balance our budget, and pay off the national debt. Our economy will boom, our citizens will prosper, and America will achieve a higher level of international prominence than ever before.</p>
    </div>
  </section>

  <section class="cover cover--front" aria-label="Front cover">
    <h1 class="title">
      <span class="title__lead">The Nine</span>
      <span class="title__main">HARBOR</span>
      <span class="title__sub">LANTERNS</span>
    </h1>
    <div class="title__rule"></div>

    <svg class="artwork" viewBox="0 0 330 300" role="img" aria-label="Illustration of a white dove carrying an olive branch to a hundred dollar bill">
      <defs>
        <linearGradient id="artFill" x1="0" y1="0" x2="1" y2="1">
          <stop offset="0" stop-color="#e4efe2"/>
          <stop offset="1" stop-color="#6fb86a"/>
        </linearGradient>
      </defs>
      <rect x="0" y="0" width="330" height="300" rx="10" fill="url(#artFill)"/>
    </svg>

    <div class="author">Derek Halvorn</div>
    <div class="author__rule"></div>
    <div class="subtitle-band">
      <span class="subtitle-band__mark"></span>
      <p class="subtitle-band__text">The Patient Weave of Morning Light<br>and Quiet Harbor Stones</p>
    </div>
  </section>
</body>
</html>
```